IT services company requires Letterhead design

We need a professional letterhead designed to be used for general correspondence with customers, quotes, invoices etc. We are a new IT services company specialising in computer servicing and repairs and mobile and tablet repairs. Attached are templates that my printing company have supplied, my logos, an interpretation of our website for you to get a feel of the company. Details to be included on the letterhead are

Company Number – 4830517
VAT Number - 581736294
Registered Address – 14-16 Brambury Lane, London, E9 3PL

Phone – 01843 572236
Email – sales@quorvant.com
Web – www.quorvant.com

I would prefer for the top of the letterhead to just have the company logo on a white background and the rest of the details on the bottom of the letterhead but I am open to design ideas.

Thanks

```html
<!DOCTYPE html>
<html lang="en">
<head>
<meta charset="utf-8">
<title>Quorvant Letterhead</title>
<link rel="stylesheet" href="https://fonts.googleapis.com/css2?family=Noto+Serif&family=Open+Sans:wght@400;700&display=swap">
<style>
  :root {
    --brand-blue: #3bbcdc;
    --ink: #1a1a1a;
    --footer-black: #000000;
    --paper: #ffffff;
    --backdrop: #8a8989;
  }
  * { margin: 0; padding: 0; box-sizing: border-box; }
  html, body {
    width: 960px; height: 1200px; overflow: hidden;
    background: var(--backdrop);
  }
  .letterhead {
    position: absolute; left: 80px; top: 0;
    width: 800px; height: 1200px;
    background: var(--paper);
    font-family: "Noto Serif", Georgia, serif;
    color: var(--ink);
  }
  .header-wave { position: absolute; left: 0; top: 0; width: 800px; height: 176px; display: block; }
  .brand-name {
    position: absolute; right: 68px; top: 62px;
    font-family: "Open Sans", Arial, sans-serif;
    font-weight: 700; font-size: 52px; line-height: 1;
    color: var(--paper); letter-spacing: -0.5px;
  }
  .letter-body {
    position: absolute; left: 89px; width: 612px;
    font-size: 13.4px; line-height: 19px;
  }
  .letter-body p { position: absolute; left: 0; width: 612px; }
  .date { top: 278px; }
  .salutation { top: 372px; }
  .subject { top: 409px; }
  .para-1 { top: 447px; }
  .para-2 { top: 560px; }
  .para-3 { top: 673px; }
  .closing { top: 787px; }
  .signature {
    position: absolute; left: 0; top: 811px;
    width: 176px; height: 50px;
    background: linear-gradient(90deg, #f2f2f2, #e6e6e6);
  }
  .signatory { top: 883px; }
  .footer-band {
    position: absolute; left: 0; top: 1098px;
    width: 800px; height: 82px;
    background: var(--footer-black);
    color: var(--paper);
    font-family: "Open Sans", Arial, sans-serif;
  }
  .contact { position: absolute; font-size: 10.5px; line-height: 1; white-space: nowrap; }
  .contact-phone { left: 53px; top: 24px; }
  .contact-email { left: 171px; top: 24px; }
  .contact-web { left: 299px; top: 24px; }
  .contact-address { left: 53px; top: 45px; }
  .registration {
    position: absolute; right: 160px; top: 26px;
    font-size: 12px; line-height: 17px; text-align: right; white-space: nowrap;
  }
  .footer-badge {
    position: absolute; left: 659px; top: 1089px;
    width: 100px; height: 100px; border-radius: 50%;
    background: var(--footer-black);
    border: 4px solid var(--paper);
    box-shadow: 0 0 0 1px var(--footer-black);
    display: flex; align-items: center; justify-content: center;
    font-family: "Open Sans", Arial, sans-serif;
    font-weight: 700; font-size: 15px; color: var(--paper);
  }
</style>
</head>
<body>
  <div class="letterhead">
    <svg class="header-wave" viewBox="0 0 800 176" preserveAspectRatio="none" aria-hidden="true">
      <path d="M0 0 H800 V165 C760 170 700 172 650 168 C560 160 480 130 380 112 C260 90 150 80 80 90 C40 95 15 100 0 106 Z" fill="var(--brand-blue)"/>
    </svg>
    <div class="brand-name">Quorvant</div>

    <div class="letter-body">
      <p class="date">January 28, 2013</p>
      <p class="salutation">Dear Sir,</p>
      <p class="subject">RE: The Norvale Brand</p>
      <p class="para-1">Lorem ipsum dolor sit amet, consectetur adipisicing elit, sed do eiusmod tempor incididunt ut labore et dolore magna aliqua. Ut enim ad minim veniam, quis nostrud exercitation ullamco laboris nisi ut aliquip ex ea commodo consequat. Duis aute irure dolor in reprehenderit in voluptate velit esse cillum dolore eu fugiat nulla pariatur. Excepteur sint occaecat cupidatat non proident, sunt in culpa qui officia deserunt mollit anim id est laborum.</p>
      <p class="para-2">Sed ut perspiciatis unde omnis iste natus error sit voluptatem accusantium doloremque laudantium, totam rem aperiam, eaque ipsa quae ab illo inventore veritatis et quasi architecto beatae vitae dicta sunt explicabo. Nemo enim ipsam voluptatem quia voluptas sit aspernatur aut odit aut fugit, sed quia consequuntur magni dolores eos qui ratione voluptatem sequi nesciunt.</p>
      <p class="para-3">At vero eos et accusamus et iusto odio dignissimos ducimus qui blanditiis praesentium voluptatum deleniti atque corrupti quos dolores et quas molestias excepturi sint occaecati cupiditate non provident, similique sunt in culpa qui officia deserunt mollitia animi, id est laborum et dolorum fuga.</p>
      <p class="closing">Sincerely,</p>
      <div class="signature" role="img" aria-label="Handwritten signature of Dean Halloway"></div>
      <p class="signatory">Dean Halloway</p>
    </div>

    <footer class="footer-band">
      <span class="contact contact-phone">P – 01843 572236</span>
      <span class="contact contact-email">E – sales@quorvant.com</span>
      <span class="contact contact-web">W – www.quorvant.com</span>
      <span class="contact contact-address">A – 14-16 Brambury Lane, London, E9 3PL</span>
      <div class="registration">Company Number - 4830517<br>VAT Number - 581736294</div>
    </footer>
    <div class="footer-badge">Quorvant</div>
  </div>
</body>
</html>
```